Website for the recruitment firm vorl

Objective :

Create a modern, elegant, and understated website with a touch of sophistication. The site must be fully custom-coded (or custom-coded on WordPress), responsive, and fast, reflecting the quality and high standards of our firm.

It must be bilingual (FR/EN), with a language selector visible in the header.

About vorl.

vorl. is a high-end recruitment firm, led by experienced consultants—employees and freelancers—and supported by a dedicated team of recruitment managers. Our hybrid approach allows us to handle complex, confidential, or high-volume projects with rigor and agility.

We operate across several business verticals:

Executive

Finance & Advisory (accounting, management control, treasury, corporate finance, financial consulting or investment banking)

Legal

Audit & Expertise

People & Office

Supply & Purchasing

Industry & Engineering

Our approach is based on a balance between human know-how and cutting-edge technologies (AI, automation, data) to respond to recruitment challenges with accuracy, responsiveness and impact.

Slogan: Expertise at the service of every recruitment.

Purpose of the site:

Client side: present our expertise, our values, our support.

Candidate side: allow the search for offers, by expertise.

On the consultant side: encouraging freelancers or employees to join us.

Structure & pages requested:

Welcome

Main banner with slogan and strong visual (possibility of a background video like maltevo.ca — for a modern and dynamic look)

Clear redirection to both paths: “I’m looking for talent” / “I want to join vorl. ”

Quick presentation of expertise with redirection to each dedicated page

Highlighting values

About

Our mission

Our values (excellence, flexibility, partnership)

Our hybrid operation (in-house and independent consultants)

The recruitment team and the support offered

Expertise (1 page per vertical, with color code specific to each division)

Description of the professions recruited

Key skills

Typical customer profiles

Testimonials or case studies (placeholder)

Button/CTA to offers corresponding to this expertise

Job offers

Page with filter by expertise

“Join vorl” option with our internal offers (consultants, recruitment managers, etc.)

Join us

Why work with vorl.

Independent vs. employee path

Tools provided, support, internal training

Highlighting the support team and recruitment managers

Contact

Form

Email + ProLink link

Design requirements:

Font: Gazette LT Std or contemporary serif with a strong identity

Color code by division (the background or page elements must match the color of the expertise):

vorl. / vorl.group. → #000000 (black)

vorl.executive. → #2F4F4F (dark green)

vorl.finance&advisory. → #0B1E36 (midnight blue)

vorl.people&office. → #f2b8b8 (powder pink)

vorl.audit&expertise. → #993294 (plum)

vorl.legal. → #d9a00f (yellow gold)

vorl.supply&purchasing. → #CE8946 (rust bronze)

vorl.industry&engineering. → #9e9b9e (light silver gray)

Technical features:

100% responsive and mobile-friendly design

Fast charging

Own structure (SEO-friendly)

Simple back-office interface for updating offers

Language selector FR / EN

Inspirations to consult:

For the tree structure, tabs and ergonomics: tindle-bray.com

For visual ambiance / video / animation: maltevo.ca

Expected deliverables:

Full site (online or compressed file)

All source files (HTML/CSS/JS or custom Wordpress)

Favicon

Brand guideline (PDF) with:

Typographies used

HEX color codes

Margins and line spacing

Examples of use of light and dark background logo

Optional: template for email signature

Objective
Design a modern, elegant and clean website with a touch of sophistication. The site must be fully custom-coded (or built with custom WordPress development), responsive, fast, and reflect the premium standards and quality of our recruitment firm.

It must be bilingual (FR/EN), with a clearly visible language selector in the header.

About vorl.
vorl. is a premium recruitment firm driven by experienced consultants — whether in-house or freelance — supported by a dedicated team of recruitment coordinators. Our hybrid model allows us to handle complex, confidential, or high-volume recruitment assignments with both precision and agility.

We operate across several verticals:

Executive

Finance & Advisory (accounting, controlling, treasury, corporate finance, investment banking advisory)

Legal

Audit & Expertise

People & Office

Supply & Purchasing

Industry & Engineering

Our approach combines human expertise with cutting-edge technologies (AI, automation, data) to tackle recruitment challenges with accuracy, speed, and impact.

Tagline: Expertise serving every recruitment need.

Website Purpose
Client-facing: highlight our expertise, values, and recruitment support model.

Candidate-facing: allow job seekers to explore openings by area of expertise.

Consultant-facing: attract freelance or in-house recruiters to join vorl.

Site Structure & Required Pages
Home
Hero banner with tagline and impactful visual (option for background video, eg maltevo. That)

Clear user path: “I'm looking to hire” / “I want to join vorl. ”

Quick intro to our expertise areas with links to each division page

Highlight our values and unique model

About Us
Our mission

Our hybrid recruitment model (internal consultants + freelancers)

Our recruitment support team and how we work

Expertise (1 page per vertical, using the division's brand color)
Each division page should include:

Description of roles we recruit

Key skills

Typical client profiles

Placeholder for testimonials or success stories

CTA linking to job openings relevant to the division

Verticals:

Executive

Finance & Advisory

Legal

Audit & Expertise

People & Office

Supply & Purchasing

Industry & Engineering

Job Offers
Central job board with filter by expertise

Section: “Join vorl. ” with internal positions (consultants, recruitment coordinators, etc.)

Join Us
Why join vorl.

Independent vs. permanent contract path

Tools, training and operational support

Highlight the internal sourcing and recruitment support team

Contact
Contact form

Email + ProLink link

Design Requirements
Font: Gazette LT Std or similar contemporary serif with strong identity

Each vertical should have its own dedicated brand color applied to its page background or key elements:

Division HEX Code Color Description
vorl. /vorl.group. #000000 Black
vorl.executive #2F4F4F Dark green
vorl.finance&advisory #0B1E36 Navy blue
vorl.people&office #f2b8b8 Powder pink
vorl.audit&expertise #993294 Plum
vorl.legal #d9a00f Golden yellow
vorl.supply&purchasing #CE8946 Rust bronze
vorl. industry&engineering #9e9b9e Light silver gray

Technical Features
Fully responsive and mobile-friendly

Fast loading

Clean structure, SEO optimized

Simple back-office interface for job posting and updates

Bilingual switch: FR / EN

Inspirations
For navigation, structure, and user interface:
🔗 https://www.tindle-bray.com/fr/fr/

For visual style, animations, and dynamic video intro:
🔗 https://maltevo.ca/

Deliverables
Fully functional website (live or delivered as a complete package)

All source files (HTML/CSS/JS or custom WordPress)

Favicon

Brand guideline (PDF) including:

Fonts used

HEX color codes

Spacing and layout guidelines

Logo usage on dark/light backgrounds

Optional: email signature template

Target Market(s)

Recruitment firm environment

Industry/Entity Type

Hi, A few clarifications to guide the website structure. The site should be clearly built around three main sections, each addressing a specific target audience: 1. For Clients – “Looking to hire?” This section will highlight our recruitment services, industry expertise, and tailored approach. 2. For Candidates – “Looking for a job?” A space where candidates can explore job offers by sector and apply directly. 3. For Experts – “Want to join us?” This area is for recruitment professionals (consultants or talent acquisition specialists) interested in joining vorl., either as employees or as independents. It should showcase the tools, support, and working environment we offer. These three user paths should be clearly visible on the homepage, using clear buttons or dedicated sections to ensure smooth navigation.

Coding

Coded - Design and coding required

Number of Pages Required

5+ page

Font styles to use
Other font styles liked:
• Gazette LT Std

Colors

Designer to choose colors to be used in the design.

Requirements
Must have
• Essentials – Section Ideas Our hybrid model → Clear presentation of employee/freelance cohabitation, and how it brings flexibility and efficiency to clients. Our quality commitment → Rigorous methodology, transparency, customer satisfaction, tailor-made support. Our augmented approach → Highlighting the use of AI tools, intelligent CRM, automated multi-channel sourcing, predictive tests, etc. Our support team → Promotion of the team of recruitment managers who support the consultants, guaranteeing responsiveness and depth in the hunt. Our areas of expertise → Mini-grid or mosaic that links to the main verticals (useful for cross-functional reinforcement).
Nice to have
• CRM / ATS Integration Direct connection with our application management tool (Velump type or other), for seamless synchronization of offers, applications and follow-ups. 📱 Progressive web app version (PWA) A site accessible in mobile application mode, for a smooth, fast and accessible offline user experience.

```html
<!DOCTYPE html>
<html lang="en">
<head>
<meta charset="utf-8">
<title>vorl. — Expertise at the service of every recruitment</title>
<link href="https://fonts.googleapis.com/css2?family=Libre+Caslon+Text:wght@400;700&family=Outfit:wght@300;400;500;600&display=swap" rel="stylesheet">
<style>
:root{
  --ink:#111111;
  --black:#000000;
  --cream:#f6f2e6;
  --white:#ffffff;
  --muted:#3a3a3a;
  --line:#ece8dc;
  --executive:#2F4F4F;
  --finance:#0B1E36;
  --legal:#d9a00f;
  --people:#f2b8b8;
  --star:#f4b400;
  --serif:"Libre Caslon Text", Georgia, serif;
  --sans:"Outfit", Arial, sans-serif;
}
*{box-sizing:border-box;margin:0;padding:0}
html,body{width:1200px;height:3228px;overflow:hidden}
body{font-family:var(--sans);color:var(--ink);background:var(--white);position:relative}
a{color:inherit;text-decoration:none}
section,header,footer{position:relative;width:1200px}
.btn{display:inline-flex;align-items:center;gap:8px;font-family:var(--sans);font-weight:600;font-size:12px;border-radius:3px}
.btn-dark{background:var(--black);color:var(--white);padding:0 16px;height:36px}
.btn-line{border:1.5px solid var(--ink);padding:0 8px;height:33px;font-size:12px}
.arrow{width:16px;height:8px}

/* Hero */
.hero{height:521px;overflow:hidden;color:var(--white)}
.hero-photo{position:absolute;inset:0;background:linear-gradient(100deg,#1f2a35 0%,#3b4650 40%,#6a6e70 60%,#3a4450 100%)}
.hero-shade{position:absolute;inset:0;background:linear-gradient(180deg,rgba(0,0,0,.25),rgba(0,0,0,.15) 60%,rgba(0,0,0,.35))}
.logo-box{position:absolute;left:122px;top:0;width:107px;height:79px;background:var(--cream);display:flex;align-items:center;justify-content:center;font-family:var(--serif);font-weight:700;font-size:30px;color:var(--ink);letter-spacing:-1px}
.nav{position:absolute;right:123px;top:25px;display:flex;align-items:center;gap:16px;font-size:11.5px;font-weight:600}
.nav .search{width:14px;height:14px;margin:0 10px 0 4px}
.nav .signin{background:var(--black);height:33px;padding:0 15px;display:flex;align-items:center;border-radius:3px;margin-left:6px}
.hero h1{position:absolute;left:118px;top:188px;font-family:var(--serif);font-weight:400;font-size:140px;line-height:1;letter-spacing:-2px}
.hero .sub{position:absolute;left:122px;top:326px;font-family:var(--serif);font-size:36px}
.hero .lede{position:absolute;left:122px;top:380px;font-size:16px;font-weight:300}
.play{position:absolute;left:977px;top:250px;width:100px;height:100px;border:1.5px solid rgba(255,255,255,.85);border-radius:50%;display:flex;align-items:center;justify-content:center;gap:6px;font-size:11.5px}

/* Paths */
.paths{height:153px;background:var(--cream)}
.path{position:absolute;top:28px;width:300px}
.path h3{font-family:var(--serif);font-weight:400;font-size:21px;margin-bottom:10px}
.path p{font-size:11.5px;line-height:16px;color:var(--muted);height:40px}
.path .btn-line{margin-top:8px}

/* About */
.about{height:493px}
.about-photo{position:absolute;left:122px;top:50px;width:487px;height:393px;background:linear-gradient(135deg,#c9c4b9,#8d8576 55%,#b5aa98)}
.about-copy{position:absolute;left:681px;top:66px;width:405px}
.about-copy h2{font-family:var(--serif);font-weight:400;font-size:42px;line-height:1}
.about-copy h4{font-family:var(--serif);font-weight:400;font-size:20px;margin:8px 0 24px}
.about-copy p{font-size:12.2px;line-height:18px;color:var(--muted);margin-bottom:16px}
.about-copy .btn-dark{margin-top:6px;height:37px;padding:0 27px}

/* Sectors */
.sectors{height:424px;background:var(--cream);overflow:hidden}
.sec-head{position:absolute;left:122px;top:46px}
.sec-head h2,.testi h2{font-family:var(--serif);font-weight:400;font-size:40px;line-height:1}
.sec-head p,.testi .tsub{font-family:var(--serif);font-size:19px;margin-top:6px}
.arrows{position:absolute;right:123px;display:flex;gap:7px}
.arrows span{width:40px;height:40px;border:1.5px solid var(--ink);border-radius:50%;display:flex;align-items:center;justify-content:center}
.sector{position:absolute;top:148px;width:307px;height:225px}
.sector .shot{position:absolute;inset:0}
.sector .tag{position:absolute;left:6px;bottom:6px;width:244px;height:80px;padding:9px 18px;color:var(--white)}
.sector .tag h3{font-family:var(--serif);font-weight:400;font-size:20px;margin-bottom:5px}
.sector .tag p{font-size:11.5px;line-height:17px}

/* Jobs */
.jobs{height:607px}
.jobs h2{position:absolute;top:38px;width:100%;text-align:center;font-family:var(--serif);font-weight:400;font-size:40px}
.jobs .intro{position:absolute;top:94px;width:100%;text-align:center;font-size:12px;color:var(--muted)}
.job{position:absolute;width:306px;height:166px;border:1px solid var(--line);border-radius:4px;padding:14px 17px}
.job h3{font-family:var(--serif);font-weight:400;font-size:14px;margin-bottom:6px}
.job .desc{font-size:11.3px;color:var(--muted)}
.job .loc{display:flex;align-items:center;gap:6px;font-size:11px;margin:14px 0 10px}
.chips{display:flex;gap:10px;margin-bottom:9px}
.chip{display:inline-flex;align-items:center;gap:6px;background:#f8f7f3;padding:3px 6px;font-size:9.5px;color:var(--muted)}
.chip i{width:11px;height:12px;background:#444;display:inline-block;border-radius:1px}
.jobs .more{position:absolute;left:522px;top:521px;height:36px;width:155px;justify-content:center}

/* Testimonials */
.testi{height:432px;background:var(--cream)}
.testi .head{position:absolute;left:122px;top:48px}
.review{position:absolute;top:137px;width:307px;height:175px;background:var(--white);border-radius:4px;padding:25px 24px}
.review .name{font-size:12.5px;font-weight:500}
.review .date{font-size:11px;color:var(--muted);margin-top:1px}
.review .stars{display:flex;gap:3px;margin-top:5px}
.review .badge{position:absolute;right:22px;top:22px;width:48px;height:48px;border-radius:50%;background:#f1f1f1}
.review blockquote{font-size:11px;line-height:17.5px;color:var(--muted);margin-top:22px}
.testi .cta{position:absolute;left:522px;top:346px;height:36px;width:155px;justify-content:center}

/* Banner CTA */
.discover{height:312px;background:#e5e5e9;overflow:hidden}
.discover-photo{position:absolute;left:530px;top:0;width:670px;height:312px;background:radial-gradient(ellipse at 55% 50%,#c9cbd1 0%,#dcdde2 55%,#e5e5e9 80%)}
.discover-copy{position:absolute;left:122px;top:54px;width:420px}
.discover-copy h2{font-family:var(--serif);font-weight:400;font-size:40px;line-height:43px}
.discover-copy p{font-size:12px;line-height:18px;color:var(--muted);margin:24px 0 20px}
.discover-copy .btn-dark{height:37px;padding:0 20px}

/* Footer */
.footer{height:286px;background:var(--black);color:var(--white)}
.f-logo{position:absolute;left:122px;top:50px;font-family:var(--serif);font-weight:700;font-size:34px;letter-spacing:-1px}
.f-about{position:absolute;left:122px;top:103px;width:310px;font-size:11px;line-height:17.5px;color:#ddd}
.f-col{position:absolute;top:56px}
.f-col h5{font-family:var(--serif);font-weight:700;font-size:13px;margin-bottom:12px}
.f-col li{list-style:none;font-size:10.8px;line-height:22.5px;color:#e5e5e5;display:flex;gap:7px;align-items:flex-start}
.f-col .dot{width:8px;height:8px;background:#fff;margin-top:7px;border-radius:1px;flex:none}
.f-rule{position:absolute;left:122px;right:123px;top:236px;height:1px;background:#333}
.f-base{position:absolute;left:122px;right:123px;top:252px;display:flex;justify-content:space-between;font-size:10.5px}
.f-base nav{display:flex;gap:8px}
</style>
</head>
<body>

<header class="hero">
  <div class="hero-photo" role="img" aria-label="Consultants meeting around a table in a glass-walled office"></div>
  <div class="hero-shade"></div>
  <div class="logo-box">vorl.</div>
  <nav class="nav">
    <a href="#">Home</a><a href="#">About Us</a><a href="#">Expertise</a><a href="#">Job offers</a><a href="#">Contact Us</a>
    <svg class="search" viewBox="0 0 14 14" fill="none" stroke="#fff" stroke-width="1.6"><circle cx="6" cy="6" r="4.6"/><path d="M9.5 9.5L13 13"/></svg>
    <a class="signin" href="#">Sign In / Register</a>
  </nav>
  <h1>Expertise</h1>
  <p class="sub">At the service of every recruitment</p>
  <p class="lede">Connecting skilled professionals with top employers across industries.</p>
  <a class="play" href="#"><svg width="12" height="13" viewBox="0 0 12 13"><path d="M1 1L11 6.5L1 12Z" fill="#fff"/></svg>Play Video</a>
</header>

<section class="paths">
  <div class="path" style="left:122px">
    <h3>I’m Looking For Talent</h3>
    <p>Looking to hire? Find skilled professionals fast. Post your job and start hiring today.</p>
    <a class="btn btn-line" href="#">Learn More <svg class="arrow" viewBox="0 0 16 8" fill="none" stroke="#111" stroke-width="1.3"><path d="M0 4H15M11 0.5L15 4L11 7.5"/></svg></a>
  </div>
  <div class="path" style="left:463px">
    <h3>I’m Looking For A Job</h3>
    <p>Your next opportunity is just a few clicks away. Browse job listings from top companies.</p>
    <a class="btn btn-line" href="#">Learn More <svg class="arrow" viewBox="0 0 16 8" fill="none" stroke="#111" stroke-width="1.3"><path d="M0 4H15M11 0.5L15 4L11 7.5"/></svg></a>
  </div>
  <div class="path" style="left:819px">
    <h3>I Want To Join vorl</h3>
    <p>Want to join us? Ready to take the next step in your career? Let vorl help you get there.</p>
    <a class="btn btn-line" href="#">Learn More <svg class="arrow" viewBox="0 0 16 8" fill="none" stroke="#111" stroke-width="1.3"><path d="M0 4H15M11 0.5L15 4L11 7.5"/></svg></a>
  </div>
</section>

<section class="about">
  <div class="about-photo" role="img" aria-label="Team of recruiters working together around a meeting table, seen from above"></div>
  <div class="about-copy">
    <h2>About vorl</h2>
    <h4>Executive &amp; elite talent recruitment</h4>
    <p>vorl. is a high-end recruitment firm, led by experienced consultants - employees and freelancers—and supported by a dedicated team of recruitment managers. Our hybrid approach allows us to handle complex, confidential, or high-volume projects with rigor and agility.</p>
    <p>Lorem ipsum dolor sit amet, consectetur adipiscing elit, sed do eiusmod tempor incididunt ut labore et dolore magna aliqua. Ut enim ad minim veniam, quis nostrud exercitation ullamco laboris nisi ut aliquip ex ea com modo consequat. Duis aute irure dolor in reprehenderit in voluptate velit esse cillum dolore eu fugiat nulla pariatur. Excepteur sint occaecat cupida tat non proident, sunt in culpa qui officia deserunt mollit anim id est laborum.</p>
    <a class="btn btn-dark" href="#">More About Us <svg class="arrow" viewBox="0 0 16 8" fill="none" stroke="#fff" stroke-width="1.3"><path d="M0 4H15M11 0.5L15 4L11 7.5"/></svg></a>
  </div>
</section>

<section class="sectors">
  <div class="sec-head">
    <h2>Our Core Sectors</h2>
    <p>We operate across several business verticals:</p>
  </div>
  <div class="arrows" style="top:77px">
    <span><svg class="arrow" viewBox="0 0 16 8" fill="none" stroke="#111" stroke-width="1.3"><path d="M16 4H1M5 0.5L1 4L5 7.5"/></svg></span>
    <span><svg class="arrow" viewBox="0 0 16 8" fill="none" stroke="#111" stroke-width="1.3"><path d="M0 4H15M11 0.5L15 4L11 7.5"/></svg></span>
  </div>
  <article class="sector" style="left:122px">
    <div class="shot" role="img" aria-label="Two executives shaking hands in an office" style="background:linear-gradient(135deg,#3d4a55,#8a9098 55%,#b9c7d6)"></div>
    <div class="tag" style="background:var(--executive)"><h3>Executive</h3><p>Lorem ipsum dolor sit amet, consectetur adipiscing elit.</p></div>
  </article>
  <article class="sector" style="left:447px">
    <div class="shot" role="img" aria-label="Laptop showing financial dashboards" style="background:linear-gradient(135deg,#6c7276,#c8ccd0 50%,#3e3a36)"></div>
    <div class="tag" style="background:var(--finance)"><h3>Finance &amp; Advisory</h3><p>Lorem ipsum dolor sit amet, consectetur adipiscing elit.</p></div>
  </article>
  <article class="sector" style="left:772px">
    <div class="shot" role="img" aria-label="Scales of justice and law books on a desk" style="background:linear-gradient(135deg,#3a2116,#7a4a2a 50%,#2a1a12)"></div>
    <div class="tag" style="background:var(--legal)"><h3>Legal &amp; Compliance</h3><p>Lorem ipsum dolor sit amet, consectetur adipiscing elit.</p></div>
  </article>
  <article class="sector" style="left:1097px">
    <div class="shot" role="img" aria-label="Office colleagues collaborating" style="background:linear-gradient(135deg,#4a4636,#8a8060 60%,#5a5444)"></div>
    <div class="tag" style="background:var(--people)"><h3>People &amp; Office</h3><p>Lorem ipsum dolor sit amet, consectetur adipiscing elit.</p></div>
  </article>
</section>

<section class="jobs">
  <h2>Access The Best Opportunities</h2>
  <p class="intro">Lorem ipsum dolor sit amet, consectetur adipiscing elit, sed do eiusmod tempor incididunt ut labore et dolore magna aliqua.</p>

  <article class="job" style="left:122px;top:135px">
    <h3>Chartered Accountant (M/F)</h3><p class="desc">Lorem ipsum dolor sit amet, consectetur adipiscing</p>
    <p class="loc"><svg width="10" height="13" viewBox="0 0 10 13"><path d="M5 0.5A4.3 4.3 0 0 0 0.7 4.8C0.7 8 5 12.5 5 12.5S9.3 8 9.3 4.8A4.3 4.3 0 0 0 5 0.5Z" fill="#111"/><circle cx="5" cy="4.8" r="1.6" fill="#fff"/></svg>France</p>
    <div class="chips"><span class="chip"><i></i>Audit &amp; Accounting Expertise</span><span class="chip"><i></i>CDI</span></div>
    <span class="chip"><i></i>from 45,000 EUR to 50,000 EUR per year+</span>
  </article>
  <article class="job" style="left:447px;top:135px">
    <h3>Project Management Analyst (M/F)</h3><p class="desc">Lorem ipsum dolor sit amet, consectetur adipiscing</p>
    <p class="loc"><svg width="10" height="13" viewBox="0 0 10 13"><path d="M5 0.5A4.3 4.3 0 0 0 0.7 4.8C0.7 8 5 12.5 5 12.5S9.3 8 9.3 4.8A4.3 4.3 0 0 0 5 0.5Z" fill="#111"/><circle cx="5" cy="4.8" r="1.6" fill="#fff"/></svg>France</p>
    <div class="chips"><span class="chip"><i></i>Administrative</span><span class="chip"><i></i>CDI</span></div>
    <span class="chip"><i></i>from 45,000 EUR to 50,000 EUR per year+</span>
  </article>
  <article class="job" style="left:772px;top:135px">
    <h3>Junior Accounting Assistant (M/F)</h3><p class="desc">Lorem ipsum dolor sit amet, consectetur adipiscing</p>
    <p class="loc"><svg width="10" height="13" viewBox="0 0 10 13"><path d="M5 0.5A4.3 4.3 0 0 0 0.7 4.8C0.7 8 5 12.5 5 12.5S9.3 8 9.3 4.8A4.3 4.3 0 0 0 5 0.5Z" fill="#111"/><circle cx="5" cy="4.8" r="1.6" fill="#fff"/></svg>France</p>
    <div class="chips"><span class="chip"><i></i>Audit &amp; Accounting Expertise</span><span class="chip"><i></i>CDI</span></div>
    <span class="chip"><i></i>from 45,000 EUR to 50,000 EUR per year+</span>
  </article>
  <article class="job" style="left:122px;top:322px">
    <h3>Accounting Assistant (M/F)</h3><p class="desc">Lorem ipsum dolor sit amet, consectetur adipiscing</p>
    <p class="loc"><svg width="10" height="13" viewBox="0 0 10 13"><path d="M5 0.5A4.3 4.3 0 0 0 0.7 4.8C0.7 8 5 12.5 5 12.5S9.3 8 9.3 4.8A4.3 4.3 0 0 0 5 0.5Z" fill="#111"/><circle cx="5" cy="4.8" r="1.6" fill="#fff"/></svg>France</p>
    <div class="chips"><span class="chip"><i></i>Audit &amp; Accounting Expertise</span><span class="chip"><i></i>CDI</span></div>
    <span class="chip"><i></i>from 45,000 EUR to 50,000 EUR per year+</span>
  </article>
  <article class="job" style="left:447px;top:322px">
    <h3>Memorialist Chartered Accountant (M/F)</h3><p class="desc">Lorem ipsum dolor sit amet, consectetur adipiscing</p>
    <p class="loc"><svg width="10" height="13" viewBox="0 0 10 13"><path d="M5 0.5A4.3 4.3 0 0 0 0.7 4.8C0.7 8 5 12.5 5 12.5S9.3 8 9.3 4.8A4.3 4.3 0 0 0 5 0.5Z" fill="#111"/><circle cx="5" cy="4.8" r="1.6" fill="#fff"/></svg>France</p>
    <div class="chips"><span class="chip"><i></i>Audit &amp; Accounting Expertise</span><span class="chip"><i></i>CDI</span></div>
    <span class="chip"><i></i>from 45,000 EUR to 50,000 EUR per year+</span>
  </article>
  <article class="job" style="left:772px;top:322px">
    <h3>Experienced Accounting Assistant (M/F)</h3><p class="desc">Lorem ipsum dolor sit amet, consectetur adipiscing</p>
    <p class="loc"><svg width="10" height="13" viewBox="0 0 10 13"><path d="M5 0.5A4.3 4.3 0 0 0 0.7 4.8C0.7 8 5 12.5 5 12.5S9.3 8 9.3 4.8A4.3 4.3 0 0 0 5 0.5Z" fill="#111"/><circle cx="5" cy="4.8" r="1.6" fill="#fff"/></svg>France</p>
    <div class="chips"><span class="chip"><i></i>Audit &amp; Accounting Expertise</span><span class="chip"><i></i>CDI</span></div>
    <span class="chip"><i></i>from 45,000 EUR to 50,000 EUR per year+</span>
  </article>

  <a class="btn btn-dark more" href="#">See More Job Offer <svg class="arrow" viewBox="0 0 16 8" fill="none" stroke="#fff" stroke-width="1.3"><path d="M0 4H15M11 0.5L15 4L11 7.5"/></svg></a>
</section>

<section class="testi">
  <div class="head">
    <h2>Client Testimonials</h2>
    <p class="tsub">Trusted by leaders. Chosen by top talent</p>
  </div>
  <div class="arrows" style="top:69px">
    <span><svg class="arrow" viewBox="0 0 16 8" fill="none" stroke="#111" stroke-width="1.3"><path d="M16 4H1M5 0.5L1 4L5 7.5"/></svg></span>
    <span><svg class="arrow" viewBox="0 0 16 8" fill="none" stroke="#111" stroke-width="1.3"><path d="M0 4H15M11 0.5L15 4L11 7.5"/></svg></span>
  </div>

  <article class="review" style="left:122px">
    <p class="name">Marc Delorme</p><p class="date">Posted on 16 / 06 / 2024</p>
    <div class="stars"><svg width="80" height="13" viewBox="0 0 80 13" fill="#f4b400"><path id="st" d="M6.5 0.5L8.2 4.5L12.5 4.8L9.2 7.6L10.2 12L6.5 9.6L2.8 12L3.8 7.6L0.5 4.8L4.8 4.5Z"/><use href="#st" x="16.5"/><use href="#st" x="33"/><use href="#st" x="49.5"/><use href="#st" x="66"/></svg></div>
    <span class="badge"></span>
    <blockquote>“Unlike other agencies, vorl truly listened to my career goals and presented only the right-fit roles. Their guidance made all the difference in my leader-ship move. They helped me.”</blockquote>
  </article>
  <article class="review" style="left:447px">
    <p class="name">Marc Delorme</p><p class="date">Posted on 16 / 06 / 2024</p>
    <div class="stars"><svg width="80" height="13" viewBox="0 0 80 13" fill="#f4b400"><use href="#st"/><use href="#st" x="16.5"/><use href="#st" x="33"/><use href="#st" x="49.5"/><use href="#st" x="66"/></svg></div>
    <span class="badge"></span>
    <blockquote>“Unlike other agencies, vorl truly listened to my career goals and presented only the right-fit roles. Their guidance made all the difference in my leader-ship move. They helped me.”</blockquote>
  </article>
  <article class="review" style="left:772px">
    <p class="name">Marc Delorme</p><p class="date">Posted on 16 / 06 / 2024</p>
    <div class="stars"><svg width="80" height="13" viewBox="0 0 80 13" fill="#f4b400"><use href="#st"/><use href="#st" x="16.5"/><use href="#st" x="33"/><use href="#st" x="49.5"/><use href="#st" x="66"/></svg></div>
    <span class="badge"></span>
    <blockquote>“Unlike other agencies, vorl truly listened to my career goals and presented only the right-fit roles. Their guidance made all the difference in my leader-ship move. They helped me.”</blockquote>
  </article>

  <a class="btn btn-dark cta" href="#">Give Us Your Opinion <svg class="arrow" viewBox="0 0 16 8" fill="none" stroke="#fff" stroke-width="1.3"><path d="M0 4H15M11 0.5L15 4L11 7.5"/></svg></a>
</section>

<section class="discover">
  <div class="discover-photo" role="img" aria-label="Two professionals seated in red armchairs reviewing a tablet, seen from above"></div>
  <div class="discover-copy">
    <h2>Ready to Discover Exceptional Talent?</h2>
    <p>Our approach is based on a balance between human know-how and cutting-edge technologies (AI, automation, data) to respond to recruitment challenges with accuracy, responsiveness and impact.</p>
    <a class="btn btn-dark" href="#">Join the Network <svg class="arrow" viewBox="0 0 16 8" fill="none" stroke="#fff" stroke-width="1.3"><path d="M0 4H15M11 0.5L15 4L11 7.5"/></svg></a>
  </div>
</section>

<footer class="footer">
  <div class="f-logo">vorl.</div>
  <p class="f-about">Connecting exceptional talent with industry-leading organizations through executive search, strategic recruitment, and sector-specific expertise.</p>
  <div class="f-col" style="left:510px"><h5>Quick Links</h5><ul><li>Home</li><li>Services</li><li>Join the Network</li><li>Find Talent</li><li>Contact</li></ul></div>
  <div class="f-col" style="left:641px"><h5>Company</h5><ul><li>About Us</li><li>History And Values</li><li>Our Offices</li><li>Resources</li><li>Sectors Of Activity</li></ul></div>
  <div class="f-col" style="left:784px"><h5>Contact us</h5><ul>
    <li><svg width="9" height="12" viewBox="0 0 10 13" style="margin-top:6px;flex:none"><path d="M5 0.5A4.3 4.3 0 0 0 0.7 4.8C0.7 8 5 12.5 5 12.5S9.3 8 9.3 4.8A4.3 4.3 0 0 0 5 0.5Z" fill="#fff"/><circle cx="5" cy="4.8" r="1.6" fill="#000"/></svg><span style="line-height:17px;padding-top:3px">Headoffice:<br>vorl, 18 rue Lamarck<br>75018 Paris</span></li>
    <li style="margin-top:8px"><svg width="10" height="10" viewBox="0 0 10 10" style="margin-top:7px;flex:none"><path d="M2 0.5L3.8 2.8L2.8 4.2C3.5 5.6 4.4 6.5 5.8 7.2L7.2 6.2L9.5 8L8.4 9.5C4.3 9.2 0.8 5.7 0.5 1.6Z" fill="#fff"/></svg>Call us:&nbsp; +33 (0) 1 23 45 67 80</li>
    <li><svg width="10" height="8" viewBox="0 0 10 8" style="margin-top:8px;flex:none"><rect x="0.5" y="0.5" width="9" height="7" fill="#fff"/><path d="M0.5 0.8L5 4.5L9.5 0.8" stroke="#000" fill="none"/></svg>Email: info@vorl.com</li>
  </ul></div>
  <div class="f-col" style="left:997px"><h5>Social Links</h5><ul>
    <li><span class="dot"></span>Chirper</li><li><span class="dot"></span>Friendbook</li><li><span class="dot"></span>Snapframe</li><li><span class="dot"></span>ProLink</li>
  </ul></div>
  <div class="f-rule"></div>
  <div class="f-base"><span>© 2025 vorl. All rights reserved. (English)</span><nav><a href="#">Privacy Notice</a><a href="#">Terms of Use</a><a href="#">Regulatory Disclosures</a></nav></div>
</footer>

</body>
</html>
```